Wardoona Contracting Pty Ltd.

We need a corporate brand/logo for a new company. The company is represented by Indigenous Australians in Western Australias far north West. The aea is the Kimberley. The work we are involved in is contracting our services to companies. Our services range from heavy earth working machinary to landscape rehabilitation including revegetation. Other services we provide are demolition, contaminated sites and water management. We are essentially a services provider for hire. We tender mostly for contracts wit hmining companies.

```html
<!DOCTYPE html>
<html lang="en">
<head>
<meta charset="utf-8">
<title>Wardoona Contracting – Business Card</title>
<link href="https://fonts.googleapis.com/css2?family=Montserrat:wght@400;600;700&display=swap" rel="stylesheet">
<style>
  :root {
    --backdrop: #d6c0b4;
    --card: #efe5d5;
    --brand-red: #c4383a;
    --ink: #2a282c;
    --ink-soft: #4a4649;
    --card-shadow: rgba(60, 35, 25, 0.22);
  }
  * { box-sizing: border-box; margin: 0; padding: 0; }
  html, body {
    width: 1200px;
    height: 900px;
    overflow: hidden;
    background: var(--backdrop);
    font-family: "Montserrat", Arial, sans-serif;
    color: var(--ink);
  }
  .stage {
    width: 1200px;
    height: 900px;
    display: flex;
    flex-direction: column;
    align-items: center;
    justify-content: center;
    gap: 40px;
  }
  .card {
    position: relative;
    width: 660px;
    height: 390px;
    background: var(--card);
    box-shadow: 0 10px 28px var(--card-shadow);
    overflow: hidden;
  }

  /* Front */
  .card--front {
    display: flex;
    align-items: center;
    justify-content: center;
    padding-top: 60px;
  }
  .wordmark {
    display: flex;
    align-items: center;
    gap: 14px;
    white-space: nowrap;
  }
  .wordmark__dot {
    width: 30px;
    height: 30px;
    border-radius: 50%;
    background: var(--brand-red);
    flex: none;
  }
  .wordmark__name {
    font-weight: 700;
    font-size: 32px;
    letter-spacing: 1.5px;
    color: var(--brand-red);
    text-transform: uppercase;
  }

  /* Back */
  .card--back .wordmark {
    position: absolute;
    left: 36px;
    top: 120px;
    gap: 10px;
  }
  .card--back .wordmark__dot { width: 22px; height: 22px; }
  .card--back .wordmark__name { font-size: 24px; letter-spacing: 1px; }

  .holder {
    position: absolute;
    left: 36px;
    top: 222px;
    white-space: nowrap;
  }
  .holder__name {
    font-weight: 700;
    font-size: 17px;
    letter-spacing: 0.5px;
    color: var(--ink);
  }
  .holder__role {
    font-weight: 400;
    font-size: 17px;
    color: var(--ink-soft);
    line-height: 1.2;
  }

  .contact {
    position: absolute;
    left: 290px;
    top: 180px;
    list-style: none;
    display: flex;
    flex-direction: column;
    gap: 12px;
  }
  .contact__item {
    display: flex;
    align-items: center;
    gap: 10px;
    font-size: 16px;
    letter-spacing: 0.5px;
    color: var(--ink);
    white-space: nowrap;
  }
  .contact__icon {
    width: 24px;
    height: 24px;
    flex: none;
  }
</style>
</head>
<body>
<main class="stage">

  <section class="card card--front" aria-label="Business card front">
    <div class="wordmark">
      <span class="wordmark__dot" aria-hidden="true"></span>
      <span class="wordmark__name">Wardoona Contracting</span>
    </div>
  </section>

  <section class="card card--back" aria-label="Business card back">
    <div class="wordmark">
      <span class="wordmark__dot" aria-hidden="true"></span>
      <span class="wordmark__name">Wardoona Contracting</span>
    </div>

    <div class="holder">
      <p class="holder__name">First Name LastName</p>
      <p class="holder__role">Position</p>
    </div>

    <ul class="contact">
      <li class="contact__item">
        <svg class="contact__icon" viewBox="0 0 26 26" aria-hidden="true">
          <circle cx="13" cy="13" r="13" fill="var(--brand-red)"/>
          <path d="M9 7.5c.6-.4 1.3-.3 1.7.3l1.2 1.8c.3.5.2 1.1-.2 1.5l-.8.7c.6 1.4 1.7 2.6 3.1 3.3l.7-.8c.4-.4 1-.5 1.5-.2l1.8 1.2c.6.4.7 1.1.3 1.7l-.8 1c-.6.7-1.6.9-2.5.5-3.3-1.4-5.7-3.9-7.1-7.2-.3-.8-.1-1.8.6-2.4z" fill="#fff"/>
        </svg>
        <span>00 0000 0000</span>
      </li>
      <li class="contact__item">
        <svg class="contact__icon" viewBox="0 0 26 26" aria-hidden="true">
          <circle cx="13" cy="13" r="13" fill="var(--brand-red)"/>
          <rect x="7" y="9" width="12" height="8.5" rx="1" fill="none" stroke="#fff" stroke-width="1.6"/>
          <path d="M7.5 9.5 13 14l5.5-4.5" fill="none" stroke="#fff" stroke-width="1.6"/>
        </svg>
        <span>email@website.com</span>
      </li>
      <li class="contact__item">
        <svg class="contact__icon" viewBox="0 0 26 26" aria-hidden="true">
          <circle cx="13" cy="13" r="13" fill="var(--brand-red)"/>
          <path d="M13 6.5a4.3 4.3 0 0 0-4.3 4.3c0 3.2 4.3 8 4.3 8s4.3-4.8 4.3-8A4.3 4.3 0 0 0 13 6.5z" fill="#fff"/>
          <circle cx="13" cy="10.8" r="1.6" fill="var(--brand-red)"/>
        </svg>
        <span>123 Hello World Address line here</span>
      </li>
      <li class="contact__item">
        <svg class="contact__icon" viewBox="0 0 26 26" aria-hidden="true">
          <circle cx="13" cy="13" r="13" fill="var(--brand-red)"/>
          <circle cx="13" cy="13" r="6" fill="none" stroke="#fff" stroke-width="1.5"/>
          <ellipse cx="13" cy="13" rx="2.6" ry="6" fill="none" stroke="#fff" stroke-width="1.3"/>
          <path d="M7 13h12" stroke="#fff" stroke-width="1.3"/>
        </svg>
        <span>www.website.com</span>
      </li>
    </ul>
  </section>

</main>
</body>
</html>
```